Web Design Project

Need a web design to be built by in-house team of developers. I need the look and feel of the site done ready for the developers to take over.

The site is a crowd funding site like www.pledgeloft.example. Our site will have all the main functions provided for on this site.
We are not looking for sophisticated investors, instead we are looking for people with an interest in investing but that need a lot of help and support through the process.

I have already obtained the logo. I attach it here.

I also want to have a coming soon page designed. I have sketched out what i want here and am uploading it in excel. this is obviously very basic and not what i will want for the main site.

colours should be light and accessible: blues, greens, yellows.

Site is to be fun and accessible.

site will have a lot of communication based aspects needed.

I am looking for a long term relationship with a designer to do this and to do many more things. I will have a lot of banners and desgin work to do here, and am looking ONLY for someone that can work on an ongoing basis (not full time, but a few hours a week).

I am also after an animation - basic 2 minute intro - not full animation, part powerpoint and part animation. I have made a separate tender for this, please quote me on it. I want the same person doing them all preferably....
Updates

Hi all

I am impressed with some of these designs. I have uploaded the wireframe of the coming soon page. 

I prefer the designs so far that are utilizing our little icons etc. 

obviously i understand you havent got root access or anything yet so are struggling to put them in, but its worth a try, some of the designs are using them well. 

i like bright colours. 

i would also show me how you are going to design other aspects eg chat box, forum page etc. 

Industry/Entity Type

Communication

Requirements
Must have
• the site will have all the functions of www.pledgeloft.example and www.venturibay.example.

```html
<!DOCTYPE html>
<html lang="en">
<head>
<meta charset="utf-8">
<title>Ideavale – Crowdfunding for entrepreneurs</title>
<link rel="stylesheet" href="https://fonts.googleapis.com/css2?family=Alegreya:wght@700&family=Noto+Sans:wght@400;700&family=PT+Sans:wght@400;700&display=swap">
<style>
:root{
  --gold:#d9a13a;
  --orange:#f0a43a;
  --orange-dark:#e08c1c;
  --login-field:#4a3410;
  --brown-text:#5a3a08;
  --blue:#1e6b9a;
  --blue-dark:#0f4f78;
  --blue-light:#3c93c6;
  --teal:#3d8a9a;
  --navy-text:#1f4f74;
  --ink:#111;
  --grey-text:#555;
  --panel:#dcdcdc;
  --panel-light:#ececec;
  --footer:#1b1b1b;
  --white:#fff;
}
*{margin:0;padding:0;box-sizing:border-box}
html,body{width:980px;height:1200px;overflow:hidden}
body{position:relative;background:linear-gradient(#f4f4f4 0,#e6e6e6 260px,#f7f7f7 900px,#f0f0f0 1100px);font-family:"Noto Sans",Verdana,sans-serif;color:var(--ink)}
.abs{position:absolute}

/* header */
.header{left:0;top:0;width:980px;height:85px;background:linear-gradient(#fff,#eef0f2);border-top:5px solid var(--gold)}
.brand{left:113px;top:24px;display:flex;align-items:center;gap:12px}
.brand-mark{width:40px;height:40px;background:var(--blue)}
.brand-name{font-family:"PT Sans",sans-serif;font-weight:700;font-size:38px;color:#2b2b2b;line-height:1}
.login{left:434px;top:0;width:434px;height:44px;background:var(--orange);border-radius:0 0 6px 6px}
.field{top:14px;height:18px;background:var(--login-field);border-radius:4px;color:#e9d7b8;font-size:10.5px;padding:2px 5px;font-family:"Noto Sans",sans-serif}
.btn-login{left:237px;top:14px;width:43px;height:18px;background:#8a7a62;border-radius:4px;color:#222;font-size:10px;text-align:center;line-height:18px}
.btn-social{left:299px;top:7px;width:107px;height:16px;background:#3b5a9a;border:1px solid #2a4580;color:#fff;font-size:8.5px;line-height:14px;padding-left:4px;display:flex;gap:4px;align-items:center}
.btn-social i{width:10px;height:10px;background:#fff;display:block}
.login-links{left:286px;top:26px;font-size:10px;color:var(--brown-text)}

/* nav */
.nav{left:0;top:85px;width:980px;height:31px;background:linear-gradient(#4b9fce,#1d6ea0 55%,#165d8c)}
.nav a{position:absolute;top:9px;color:var(--white);font-family:"Alegreya",serif;font-weight:700;font-size:12px;text-decoration:none;letter-spacing:.3px}
.search{left:706px;top:7px;width:162px;height:18px;background:#fff;border-radius:4px;font-size:11px;color:#888;padding:1px 8px}
.search svg{position:absolute;right:4px;top:3px}

/* banner */
.banner{left:0;top:116px;width:980px;height:102px;background:radial-gradient(circle at 20% 40%,#5aa6b4 0,transparent 45%),radial-gradient(circle at 75% 60%,#4f9cad 0,transparent 45%),linear-gradient(#3f8ea0,#2f7b8f);border-bottom:2px solid #2a6f92}
.banner h1{left:111px;top:18px;font-family:"Alegreya",serif;font-size:25px;color:#fff;font-weight:700}
.banner p{left:113px;top:50px;font-family:"Alegreya",serif;font-weight:700;font-size:16px;color:var(--orange)}
.btn-learn{left:740px;top:37px;width:128px;height:30px;border-radius:15px;background:linear-gradient(#f6b552,var(--orange-dark));border:1px solid #c47a14;color:#fff;font-family:"Alegreya",serif;font-weight:700;font-size:15px;line-height:28px;padding-left:9px}
.btn-learn svg{position:absolute;right:4px;top:4px}

/* content */
.content{left:111px;top:243px;width:757px;height:837px;background:#fbfbfb;box-shadow:0 0 4px rgba(0,0,0,.1)}
.section-title{left:8px;top:17px;font-family:"PT Sans",sans-serif;font-size:22px;color:#111}
.view-more{font-family:"PT Sans",sans-serif;font-size:15px;color:var(--orange-dark)}
.rule{left:8px;width:496px;height:2px;background:var(--blue)}

.pitch{width:237px;height:195px}
.pitch-name{left:3px;top:0;font-size:12px;font-weight:700;text-decoration:underline}
.pitch-logo{left:1px;top:16px;width:77px;height:79px;border:1px solid #ccc;background:#fff}
.pitch-logo span{position:absolute;left:14px;top:14px;width:48px;height:50px}
.pitch-text{left:82px;top:15px;width:160px;font-size:9.4px;line-height:10.2px;color:#111}
.pitch-text p+p{margin-top:10px}
.read-more{right:0;top:134px;font-size:9.4px}
.progress{left:0;top:147px;width:237px;height:47px;background:linear-gradient(#e4e4e4,#cfcfcf);border-radius:6px}
.progress-track{left:4px;top:7px;width:226px;height:21px;border-radius:10px;background:#fff;border:1px solid #aaa;overflow:hidden}
.progress-fill{left:0;top:0;width:40%;height:100%;background:linear-gradient(#3f94c6,#135f92);border-radius:10px}
.progress-label{left:7px;top:30px;font-size:12px;font-family:"PT Sans",sans-serif}
.progress-label em{color:var(--navy-text)}

/* sidebar */
.side-box{background:linear-gradient(#e4e4e4,#cfcfcf);border-radius:4px}
.about{left:524px;top:22px;width:223px;height:138px}
.about h2{position:absolute;left:16px;top:8px;font-family:"PT Sans",sans-serif;font-size:15px;color:#555}
.about p{position:absolute;left:16px;top:32px;width:195px;font-family:"PT Sans",sans-serif;font-size:8.6px;line-height:13px;color:#666}
.about a{position:absolute;left:16px;top:116px;font-size:8.5px;font-weight:700;color:var(--orange-dark)}
.side-heading{font-family:"Alegreya",serif;font-weight:700;font-size:18px;color:var(--navy-text)}
.newsletter{left:524px;top:172px;width:223px;height:61px}
.subscribe{left:6px;top:28px;width:211px;height:24px;background:#fff;border-radius:5px;font-family:"Alegreya",serif;font-weight:700;font-size:13px;color:#bbb;padding:3px 6px}
.blog{left:524px;top:244px;width:223px;height:316px}
.post{left:30px;width:160px;font-size:8.8px;line-height:10.2px}
.post time{display:block;font-family:"PT Sans",sans-serif;font-weight:700;font-size:10px;color:var(--orange-dark);margin-left:0}
.post b{display:block;margin-top:12px}
.post p{margin-top:10px}
.post a{display:block;text-align:right;margin-top:8px;color:#111;text-decoration:underline}
.post-divider{left:30px;top:168px;width:160px;border-top:1px dotted var(--orange)}
.payments{left:532px;top:584px;width:209px;height:43px;border:2px solid var(--orange);background:#f7f7f7}
.follow{left:524px;top:648px;width:223px;text-align:center;font-family:"Alegreya",serif;font-weight:700;font-size:16px;color:var(--navy-text)}
.social{left:539px;top:675px;display:flex;gap:2px}
.social span{width:26px;height:26px;border-radius:3px}

/* partners */
.partners{left:14px;top:728px;width:737px;height:75px;background:linear-gradient(#2b82b9,#135c8f);border-radius:3px}
.partners h3{position:absolute;left:21px;top:28px;font-family:"PT Sans",sans-serif;font-size:14px;color:#fff}
.rail{left:121px;top:2px;width:610px;height:71px;background:#f7f7f7}
.tab{top:14px;width:20px;height:46px;background:#fff;border:1px solid #bbb}
.badge{top:12px;width:75px;height:50px;background:#fff;border:1px solid #d0d0d0;border-radius:5px;box-shadow:0 1px 3px rgba(0,0,0,.2)}
.badge span{position:absolute;left:22px;top:10px;width:30px;height:30px;border-radius:50%}

/* footer */
.footer{left:0;top:1100px;width:980px;height:100px;background:var(--footer);color:#fff;font-family:"PT Sans",sans-serif;font-size:9.4px}
.footer-links{left:114px;top:17px}
.footer-links span{margin:0 4px;color:#aaa}
.legal{left:114px;top:45px;line-height:14px}
.copyright{left:660px;top:58px}
</style>
</head>
<body>

<header class="header abs">
  <div class="brand abs"><span class="brand-mark"></span><span class="brand-name">Ideavale</span></div>
  <div class="login abs">
    <div class="field abs" style="left:9px;width:109px">User ID</div>
    <div class="field abs" style="left:123px;width:109px">Password</div>
    <div class="btn-login abs">Login</div>
    <div class="btn-social abs"><i></i>Sign in with Linkbook</div>
    <div class="login-links abs">Register | Forgotten password</div>
  </div>
</header>

<nav class="nav abs">
  <a style="left:113px">INVEST</a>
  <a style="left:177px">GET INVESTMENT</a>
  <a style="left:300px">HOW IT WORKS</a>
  <a style="left:409px">ABOUT US</a>
  <a style="left:488px">BLOG</a>
  <a style="left:542px">FORUM</a>
  <div class="search abs">search
    <svg width="12" height="12" viewBox="0 0 12 12"><circle cx="5" cy="5" r="3.6" fill="none" stroke="#333" stroke-width="1.6"/><line x1="7.6" y1="7.6" x2="11" y2="11" stroke="#333" stroke-width="2"/></svg>
  </div>
</nav>

<section class="banner abs">
  <h1 class="abs">Crowdfunding for entrepreneurs</h1>
  <p class="abs">a new way to fund your dreams and help others to do the same.</p>
  <div class="btn-learn abs">Learn More
    <svg width="22" height="22" viewBox="0 0 22 22"><circle cx="11" cy="11" r="10" fill="#fff"/><path d="M9 6l5 5-5 5" fill="none" stroke="#333" stroke-width="2.4"/></svg>
  </div>
</section>

<main class="content abs">
  <h2 class="section-title abs">Featured pitches</h2>
  <span class="view-more abs" style="left:422px;top:26px">View more +</span>
  <div class="rule abs" style="top:45px"></div>

  <!-- pitch cards -->
  <article class="pitch abs" style="left:8px;top:59px">
    <div class="pitch-name abs">Company Name:</div>
    <div class="pitch-logo abs" role="img" aria-label="Company badge"><span style="background:#1d2f8a"></span></div>
    <div class="pitch-text abs"><p>Lorem Ipsum is simply dummy text of the printing and typesetting industry. Lorem Ipsum has been the industry's standard dummy text ever since the 1500s, when an unknown printer took a galley of type and</p><p>Lorem Ipsum is simply dummy text of the printing and typesetting industry. Lorem Ipsum ....</p></div>
    <span class="read-more abs">Read more</span>
    <div class="progress abs"><div class="progress-track abs"><div class="progress-fill abs"></div></div><div class="progress-label abs"><em>40%</em> invested so far</div></div>
  </article>
  <article class="pitch abs" style="left:267px;top:59px">
    <div class="pitch-name abs">Company Name:</div>
    <div class="pitch-logo abs" role="img" aria-label="Company badge"><span style="background:#c8202a"></span></div>
    <div class="pitch-text abs"><p>Lorem Ipsum is simply dummy text of the printing and typesetting industry. Lorem Ipsum has been the industry's standard dummy text ever since the 1500s, when an unknown printer took a galley of type and</p><p>Lorem Ipsum is simply dummy text of the printing and typesetting industry. Lorem Ipsum ....</p></div>
    <span class="read-more abs">Read more</span>
    <div class="progress abs"><div class="progress-track abs"><div class="progress-fill abs"></div></div><div class="progress-label abs"><em>40%</em> invested so far</div></div>
  </article>

  <article class="pitch abs" style="left:8px;top:267px">
    <div class="pitch-name abs">Company Name:</div>
    <div class="pitch-logo abs" role="img" aria-label="Company badge"><span style="background:#2c3a8e;border-radius:50%"></span></div>
    <div class="pitch-text abs"><p>Lorem Ipsum is simply dummy text of the printing and typesetting industry. Lorem Ipsum has been the industry's standard dummy text ever since the 1500s, when an unknown printer took a galley of type and</p><p>Lorem Ipsum is simply dummy text of the printing and typesetting industry. Lorem Ipsum ....</p></div>
    <span class="read-more abs">Read more</span>
    <div class="progress abs"><div class="progress-track abs"><div class="progress-fill abs"></div></div><div class="progress-label abs"><em>40%</em> invested so far</div></div>
  </article>
  <article class="pitch abs" style="left:267px;top:267px">
    <div class="pitch-name abs">Company Name:</div>
    <div class="pitch-logo abs" role="img" aria-label="Company badge"><span style="background:#e8731e"></span></div>
    <div class="pitch-text abs"><p>Lorem Ipsum is simply dummy text of the printing and typesetting industry. Lorem Ipsum has been the industry's standard dummy text ever since the 1500s, when an unknown printer took a galley of type and</p><p>Lorem Ipsum is simply dummy text of the printing and typesetting industry. Lorem Ipsum ....</p></div>
    <span class="read-more abs">Read more</span>
    <div class="progress abs"><div class="progress-track abs"><div class="progress-fill abs"></div></div><div class="progress-label abs"><em>40%</em> invested so far</div></div>
  </article>

  <article class="pitch abs" style="left:8px;top:488px">
    <div class="pitch-name abs">Company Name:</div>
    <div class="pitch-logo abs" role="img" aria-label="Company badge"><span style="background:#2a3590"></span></div>
    <div class="pitch-text abs"><p>Lorem Ipsum is simply dummy text of the printing and typesetting industry. Lorem Ipsum has been the industry's standard dummy text ever since the 1500s, when an unknown printer took a galley of type and</p><p>Lorem Ipsum is simply dummy text of the printing and typesetting industry. Lorem Ipsum ....</p></div>
    <span class="read-more abs">Read more</span>
    <div class="progress abs"><div class="progress-track abs"><div class="progress-fill abs"></div></div><div class="progress-label abs"><em>40%</em> invested so far</div></div>
  </article>
  <article class="pitch abs" style="left:267px;top:488px">
    <div class="pitch-name abs">Company Name:</div>
    <div class="pitch-logo abs" role="img" aria-label="Company badge"><span style="background:#222"></span></div>
    <div class="pitch-text abs"><p>Lorem Ipsum is simply dummy text of the printing and typesetting industry. Lorem Ipsum has been the industry's standard dummy text ever since the 1500s, when an unknown printer took a galley of type and</p><p>Lorem Ipsum is simply dummy text of the printing and typesetting industry. Lorem Ipsum ....</p></div>
    <span class="read-more abs">Read more</span>
    <div class="progress abs"><div class="progress-track abs"><div class="progress-fill abs"></div></div><div class="progress-label abs"><em>40%</em> invested so far</div></div>
  </article>

  <div class="rule abs" style="top:691px"></div>
  <span class="view-more abs" style="left:422px;top:693px">View more +</span>

  <!-- sidebar -->
  <aside class="about side-box abs">
    <h2>What is crowdfunding?</h2>
    <p>Crowdfunding is the new way for a community of like minded people to network and pool their money and knowledge together. Pledgeloft provides a platform for entrepreneurs of start-ups and established businesses to connect with potential investors.</p>
    <a>» <u>Learn more</u></a>
  </aside>

  <aside class="newsletter side-box abs">
    <h2 class="side-heading abs" style="left:9px;top:4px">Newsletter</h2>
    <div class="subscribe abs">Subscribe Here...</div>
  </aside>

  <aside class="blog side-box abs">
    <h2 class="side-heading abs" style="left:9px;top:7px">Our Latest Blog</h2>
    <div class="post abs" style="top:38px">
      <time>12-10-2011</time>
      <b>Lorem Ipsum is simply dummy text of</b>
      <p>the printing and typesetting industry. Lorem Ipsum has been the industry's standard dummy text ever since the 1500s, when an unknown ....</p>
      <a>Read more</a>
    </div>
    <div class="post-divider abs"></div>
    <div class="post abs" style="top:181px">
      <time>12-10-2011</time>
      <b>Lorem Ipsum is simply dummy text of</b>
      <p>the printing and typesetting industry. Lorem Ipsum has been the industry's standard dummy text ever since the 1500s, when an unknown ....</p>
      <a>Read more</a>
    </div>
  </aside>

  <div class="payments abs" role="img" aria-label="Accepted payment methods">
    <svg width="205" height="39" viewBox="0 0 205 39">
      <rect x="6" y="4" width="60" height="10" rx="2" fill="#1f4f8a"/>
      <rect x="6" y="21" width="24" height="13" rx="2" fill="#c33"/>
      <rect x="34" y="21" width="24" height="13" rx="2" fill="#2a66b0"/>
      <rect x="62" y="21" width="26" height="13" rx="2" fill="#1a3f8f"/>
      <rect x="92" y="21" width="26" height="13" rx="2" fill="#1a3f8f"/>
      <rect x="122" y="21" width="26" height="13" rx="2" fill="#5a9fd4"/>
      <rect x="152" y="21" width="46" height="13" rx="2" fill="#333"/>
    </svg>
  </div>

  <div class="follow abs">Follow Us</div>
  <div class="social abs" aria-label="Social links">
    <span style="background:#3b5998"></span>
    <span style="background:#4fb7e8"></span>
    <span style="background:#1b78b4"></span>
    <span style="background:#f08a24"></span>
    <span style="background:#c4302b"></span>
    <span style="background:#f47a20"></span>
    <span style="background:#12a5e0"></span>
  </div>

  <!-- partners strip -->
  <section class="partners abs">
    <h3>Our Partners:</h3>
    <div class="rail abs">
      <div class="tab abs" style="left:0;border-radius:0 12px 12px 0"><svg width="18" height="44" viewBox="0 0 18 44"><path d="M11 16l-5 6 5 6" fill="none" stroke="#1e6b9a" stroke-width="3"/></svg></div>
      <div class="tab abs" style="right:0;border-radius:12px 0 0 12px"><svg width="18" height="44" viewBox="0 0 18 44"><path d="M7 16l5 6-5 6" fill="none" stroke="#1e6b9a" stroke-width="3"/></svg></div>
      <div class="badge abs" style="left:35px" role="img" aria-label="Partner badge"><span style="background:#1f4f8a"></span></div>
      <div class="badge abs" style="left:128px" role="img" aria-label="Partner badge"><span style="background:#f29a3a"></span></div>
      <div class="badge abs" style="left:221px" role="img" aria-label="Partner badge"><span style="background:#4aa3d8"></span></div>
      <div class="badge abs" style="left:314px" role="img" aria-label="Partner badge"><span style="background:#1b4fa0;border-radius:3px"></span></div>
      <div class="badge abs" style="left:404px" role="img" aria-label="Partner badge"><span style="background:#9a9a9a;border-radius:3px"></span></div>
      <div class="badge abs" style="left:497px" role="img" aria-label="Partner badge"><span style="background:#1c3f94"></span></div>
    </div>
  </section>
</main>

<footer class="footer abs">
  <div class="footer-links abs">Contact us<span>|</span>Terms of Use<span>|</span>Privacy policy<span>|</span>Sitemap<span>|</span>FAQ<span>|</span>Partnership Opportunities<span>|</span>Press</div>
  <div class="legal abs">Pledgeloft is a registered trademark of Ideavale Limited<br>This website has been approved as a financial promotion by Harrow Lane Partners which is authorised and<br>regulated by the Financial Oversight Office.</div>
  <div class="copyright abs">Copyright 2011&nbsp; Ideavale Limited All right reserved.</div>
</footer>

</body>
</html>
```